Flyer für Tauchunternehmen
Zielgruppe
Tauchunternehmen, Taucher, Schnorchler
Aufgabenstellung
Wir sind ein Tauchunternehmen im südlichen Ägypten, mit dem Hauptaugenmerk auf unser Tauchcenter und Merohan.
Es ist mir bewusst, dass es viel Content ist. Dieser kann ggf. auch angepasst werden. Der Flyer sollte in einem gängigen Format gedruckt werden können. Lieber mehrseitig, all flächenmässig zu gross.
Die beiden erwähnten Boote gehören unbedingt zu Merohan.
Die Zip Dateien sind auf die Themen abgestimmt, resp. das allgemeine Diving kann beliebig eingesetzt werden. Je ein Exemplar in Deutsch und Englisch wäre super. Beide Texte liegen vor.
Gedruckt wird bei druckflink-kelvo.ch
Bluewake Diving Safari - Erlebe das südliche Rote Meer.
Wir zeigen euch unser tolles, vielfältiges zu Hause mit den schönsten Tauchplätzen.
Ob erfahrene Taucher oder gerade erst das Tauchabenteuer begonnen habt, erlebt mit uns die Schönheit der Unterwasserwelt mit ihren vielfältigen Korallen und Fischen.
Entfliehe mit uns dem Alltag.
Wir freuen uns, dich bei uns begrüssen zu dürfen!
Team Bluewake Diving Safari
Omar & Petra
…..and into the ocean we go, to lose our mind and find our soul
Bluewake Diving Safari - Experience the southern Red Sea.
We will show you our beautiful and diverse home with the most beautiful dive sites.
Whether you are an experienced diver or have just started your diving adventure, come with us and experience the beauty of the underwater world with its diverse corals and fish.
Escape from everyday life with us.
We look forward to welcoming you!
.....and into the ocean we go, to lose our mind and find our soul
Mit unseren Tauchcentern in El Quseir & Marsa Alam sind wir täglich am Hausriff und mit dem Minibus unterwegs für eure Tauchgänge und zum Schnorcheln. Tägliche Boot-Ausfahrte..

```html
<!DOCTYPE html>
<html lang="de">
<head>
<meta charset="utf-8">
<title>Bluewake Diving Safari – Flyer</title>
<link href="https://fonts.googleapis.com/css2?family=Quicksand:wght@500;700&family=Nunito:wght@400;600;700;800&display=swap" rel="stylesheet">
<style>
:root{
  --backdrop:#a8a8a8;
  --navy:#1f3a72;
  --navy-deep:#182e5e;
  --blue:#1e63b8;
  --blue-mid:#2f7fd0;
  --sky:#cfe3f6;
  --sky-light:#eaf3fb;
  --white:#ffffff;
  --ink:#1b2a4a;
  --accent:#3a78d6;
  --alert:#e2332b;
  --head:"Quicksand",sans-serif;
  --body:"Nunito",sans-serif;
}
*{box-sizing:border-box;margin:0;padding:0}
html,body{width:803px;height:1200px;overflow:hidden;background:var(--backdrop)}
body{position:relative;font-family:var(--body);color:var(--ink)}
.spread{position:absolute;left:20px;width:763px;height:540px;display:grid;grid-template-columns:repeat(3,1fr);box-shadow:0 4px 14px rgba(0,0,0,.25);overflow:hidden}
.spread--outside{top:25px}
.spread--inside{top:630px}
.panel{position:relative;overflow:hidden;padding:12px 14px}
.panel--light{background:linear-gradient(180deg,var(--sky-light),var(--sky))}
.panel--blue{background:linear-gradient(180deg,var(--blue),var(--blue-mid))}
.panel--navy{background:var(--navy)}
.photo{position:absolute;display:block}
.card{background:var(--white);border-radius:8px;padding:7px 9px;margin-bottom:8px;box-shadow:0 2px 4px rgba(0,0,0,.15)}
.card-title{font-family:var(--head);font-weight:700;color:var(--accent);font-size:8px;margin-bottom:3px}
.card p,.small{font-size:6.6px;line-height:1.3}
.tour-lead{font-family:var(--head);font-weight:700;color:var(--navy);font-size:12.5px;text-align:center;line-height:1.25;margin:10px 0}
/* contact */
.contact-box{margin:12px 6px 0;border:1.5px solid rgba(255,255,255,.7);border-radius:10px;padding:12px 12px 10px;color:var(--white)}
.contact-title{background:var(--white);color:var(--navy);font-family:var(--head);font-weight:700;font-size:11px;border-radius:12px;text-align:center;padding:3px 0;margin:-4px 8px 8px}
.contact-line{display:flex;align-items:center;gap:5px;font-size:8px;font-weight:600;margin:3px 0}
.social{margin:12px 6px 0}
.social-bar{display:flex;align-items:center;gap:5px;background:rgba(255,255,255,.75);color:var(--navy);font-weight:700;font-size:8px;border-radius:8px;padding:3px 8px;margin-bottom:7px}
.dot{width:7px;height:7px;border-radius:50%;background:var(--navy);flex:none}
.brand-circle{position:absolute;left:50%;bottom:18px;transform:translateX(-50%);width:120px;height:120px;border-radius:50%;background:var(--white);display:flex;align-items:center;justify-content:center;text-align:center;font-family:var(--head);font-weight:700;color:var(--navy);font-size:13px;line-height:1.2;padding:14px}
/* cover */
.cover-head{display:flex;gap:6px;align-items:flex-start}
.brand-mark{display:flex;align-items:center;gap:4px;width:80px;font-family:var(--head);font-weight:700;color:var(--navy);font-size:9px;line-height:1.15;margin-top:6px}
.brand-mark .dot{width:9px;height:9px}
.cover-title{font-family:var(--head);font-weight:700;color:var(--navy);font-size:19px;line-height:1.05;text-align:right;flex:1}
.cover-sub{font-weight:800;font-size:7px;text-align:right;color:var(--ink);margin-top:3px;line-height:1.25}
.cover-text{font-size:7px;text-align:center;line-height:1.3;margin-top:6px}
.pill{display:block;background:var(--blue);color:var(--white);font-family:var(--head);font-weight:700;font-size:10.5px;text-align:center;border-radius:10px;padding:3px 0;margin:8px 0 6px}
.cover-welcome{text-align:center;color:var(--navy);font-weight:600;font-size:8.5px;line-height:1.25}
.cover-welcome strong{display:block;font-weight:800}
.wave{position:absolute;left:0;bottom:0;width:100%}
.quote{position:absolute;left:0;right:0;bottom:14px;color:var(--white);font-size:8px;text-align:center;line-height:1.3}
/* inside */
.intro{font-size:6.8px;line-height:1.3;margin-bottom:5px}
.hotel{position:relative;height:74px;margin-bottom:6px;border-radius:8px;overflow:hidden}
.hotel-text{position:absolute;top:0;bottom:0;width:52%;background:var(--blue);color:var(--white);padding:6px 8px;border-radius:8px}
.hotel-text h3{font-family:var(--head);font-size:7.5px;font-weight:700;line-height:1.15;margin-bottom:2px}
.hotel-text p{font-size:6.3px;line-height:1.25}
.hotel .photo{top:4px;bottom:4px;width:46%;border-radius:6px;border:2px solid var(--white)}
.hotel--left .hotel-text{left:0}.hotel--left .photo{right:2px}
.hotel--right .hotel-text{right:0}.hotel--right .photo{left:2px}
.course{position:absolute;left:0;right:0;bottom:0;height:120px;background:var(--navy);color:var(--white);padding:34px 14px 0}
.course h3{font-family:var(--head);font-weight:700;color:#8ec0f0;font-size:11px;margin-bottom:3px}
.course p{font-size:7px;line-height:1.3}
.boats-title{background:var(--blue);color:var(--white);font-family:var(--head);font-weight:700;font-size:10px;text-align:center;border-radius:10px;padding:2px 0;margin-bottom:5px}
.panel--navy .small{color:var(--white)}
.boat-pair{display:flex;justify-content:center;gap:6px;margin:7px 0}
.boat-pair .photo{position:static;width:92px;height:66px;border-radius:6px;border:2px solid var(--white)}
.boat-name{color:#8ec0f0;font-weight:800;font-size:7px;margin-bottom:1px}
.note{position:absolute;left:14px;right:14px;bottom:10px;color:var(--white);font-size:6.3px;line-height:1.3}
.note .warn{color:var(--alert);font-weight:700}
.note p+p{margin-top:5px}
.stack .card{margin-bottom:7px}
</style>
</head>
<body>

<!-- outside spread -->
<section class="spread spread--outside">
  <div class="panel panel--light">
    <div class="card"><div class="card-title">Tagesboot</div><p>Fahre für einen Tag nach Merohan. Schwimme und schnorchle mit den Delfinen und geniesse ein gutes Mittagessen.</p></div>
    <div class="card"><div class="card-title">Liveaboards Tauchen</div><p>Erlebe eine fantastische Woche am Roten Meer und erkunde einige der atemberaubendsten und farbenprächtigsten Tauchplätze der Welt.</p><p style="margin-top:5px">Finde deine Lieblingsplätze mit uns im südlichen Roten Meer, Fury Shoals &amp; St. Johns.</p></div>
    <div class="card"><div class="card-title">Vollcharter Tauchen</div><p>Ihr seid eine grössere Gruppe von Tauchern oder ein Tauchclub und möchtet auf dem Boot unter euch sein? Dann kann ein Vollcharter die beste Option sein.</p></div>
    <div class="tour-lead">Die Touren beginnen und<br>enden im Hafen von Hamata.</div>
    <div class="photo" role="img" aria-label="Foto: Team und Gäste am Strand mit gesammeltem Müll nach einer Aufräumaktion" style="left:0;right:0;bottom:0;height:175px;background:linear-gradient(180deg,#7a8fa6 0%,#4b4d57 40%,#d8c7a6 75%,#c9b48e 100%)"></div>
  </div>

  <div class="panel panel--blue">
    <div class="contact-box">
      <div class="contact-title">Kontaktieren Sie uns</div>
      <div class="contact-line"><svg width="8" height="8" viewBox="0 0 10 10"><path d="M2 1l2 2-1 1.5c.6 1.2 1.3 1.9 2.5 2.5L7 6l2 2-1.2 1.5C4.5 9 1 5.5.5 2.2z" fill="#fff"/></svg>Omar +20 100 555 01 23</div>
      <div class="contact-line"><svg width="8" height="8" viewBox="0 0 10 10"><path d="M2 1l2 2-1 1.5c.6 1.2 1.3 1.9 2.5 2.5L7 6l2 2-1.2 1.5C4.5 9 1 5.5.5 2.2z" fill="#fff"/></svg>Petra +41 79 555 01 99</div>
      <div class="contact-line"><svg width="8" height="8" viewBox="0 0 10 10"><circle cx="5" cy="5" r="4" fill="none" stroke="#fff" stroke-width="1.3"/><path d="M1 5h8M5 1c2 2.5 2 5.5 0 8M5 1c-2 2.5-2 5.5 0 8" stroke="#fff" stroke-width=".8" fill="none"/></svg>www.bluewakedivingsafari.com</div>
      <div class="contact-line"><svg width="8" height="8" viewBox="0 0 10 10"><rect x="1" y="2" width="8" height="6" rx="1" fill="none" stroke="#fff" stroke-width="1.2"/><path d="M1 2.5l4 3 4-3" stroke="#fff" stroke-width="1" fill="none"/></svg>info@bluewakedivingsafari.com</div>
    </div>
    <div class="social">
      <div class="social-bar"><span class="dot"></span>bluewakediving.20</div>
      <div class="social-bar"><span class="dot"></span>bluewake_diving_safari</div>
      <div class="social-bar"><span class="dot"></span>Bluewake Diving Safari</div>
    </div>
    <div class="photo" role="img" aria-label="Foto: Delfine und Schnorchler unter Wasser" style="left:0;right:0;top:265px;height:140px;background:linear-gradient(180deg,#2b86cc,#145a9c)"></div>
    <svg class="wave" viewBox="0 0 254 150" height="150" preserveAspectRatio="none"><path d="M0 40 C80 70 170 10 254 30 L254 150 L0 150Z" fill="var(--navy)"/></svg>
    <div class="brand-circle">Bluewake Diving Safari</div>
  </div>

  <div class="panel panel--light" style="background:linear-gradient(180deg,var(--white),var(--sky))">
    <div class="cover-head">
      <div class="brand-mark"><span class="dot"></span>Bluewake Diving Safari</div>
      <div class="cover-title">Erlebe das südliche Rote Meer</div>
    </div>
    <div class="cover-sub">Wir zeigen euch unser tolles,<br>vielfältiges zu Hause mit den<br>schönsten Tauchplätzen.</div>
    <div class="cover-text">Ob erfahrene Taucher oder gerade erst das Tauchabenteuer begonnen habt, erlebt mit uns die Schönheit der Unterwasserwelt mit ihren vielfältigen Korallen und Fischen.</div>
    <span class="pill">Entfliehe mit uns dem Alltag.</span>
    <div class="cover-welcome">Wir freuen uns, dich bei uns<br>begrüssen zu dürfen!<strong>Omar &amp; Petra</strong></div>
    <div class="photo" role="img" aria-label="Foto: Tauchboot auf türkisem Wasser, darunter eine Meeresschildkröte am Grund" style="left:0;right:0;top:258px;height:250px;background:linear-gradient(180deg,#bfe2ef 0%,#4fb3cf 35%,#2a8fb3 65%,#5f8fa0 100%)"></div>
    <svg class="wave" viewBox="0 0 254 80" height="80" preserveAspectRatio="none"><path d="M0 30 C90 55 170 5 254 25 L254 80 L0 80Z" fill="var(--navy)"/></svg>
    <div class="quote">.....and into the ocean we go, to lose our<br>mind and find our soul</div>
  </div>
</section>

<!-- inside spread -->
<section class="spread spread--inside">
  <div class="panel panel--light">
    <p class="intro">Mit unseren Tauchcentern in El Quseir &amp; Marsa Alam sind wir täglich am Hausriff und mit dem Minibus unterwegs für eure Tauchgänge und zum Schnorcheln. Tägliche Boot-Ausfahrten machen wir ab Port Ghalib, Marsa Alam und Hamata.</p>
    <p class="intro">Unser Team begleitet dich professionell bei deinen ersten Atemzügen unter Wasser, bildet dich nach OWA Standard aus oder führt dich sicher entlang der Tauchplätze.</p>
    <div class="hotel hotel--left">
      <div class="hotel-text"><h3>Solmara Beach Resort, südlich von El Quseir.</h3><p>Von hier aus starten wir täglich zum Tauchen und Schnorcheln am Hausriff oder mit Minibus zu den umliegenden Riffen.</p></div>
      <div class="photo" role="img" aria-label="Foto: Hotelzimmer mit Bett" style="background:linear-gradient(135deg,#8a6a44,#c9a676)"></div>
    </div>
    <div class="hotel hotel--right">
      <div class="photo" role="img" aria-label="Foto: Taucher in Ausrüstung auf einem Steg" style="background:linear-gradient(180deg,#3aa6b5,#6b5a48)"></div>
      <div class="hotel-text"><h3>Coralis Bay Resort, südlich von El Quseir.</h3><p>Hauseigene Bucht, in der bei jedem Wetter getaucht werden kann. Eigenes Tagesboot und Speedboot.</p></div>
    </div>
    <div class="hotel hotel--left">
      <div class="hotel-text"><h3>Nereon Beach Hotel, südlich von Marsa Alam.</h3><p>Tägliche Ausflüge mit dem Minibus zu den umliegenden Riffen.</p></div>
      <div class="photo" role="img" aria-label="Foto: rote Fächerkoralle unter Wasser" style="background:linear-gradient(135deg,#2a7fa8,#8a2a3a)"></div>
    </div>
    <div class="course">
      <svg class="wave" viewBox="0 0 254 30" height="30" preserveAspectRatio="none" style="top:-1px;bottom:auto"><path d="M0 0 L254 0 L254 8 C170 28 80 -4 0 18Z" fill="var(--sky)"/></svg>
      <h3>Tauchkurse</h3>
      <p>Lerne Tauchen mit unseren passionierten Instruktoren. Als Partner von OWA bilden wir dich in allen Level von Scuba Diver bis zum Dive Master hin aus.</p>
    </div>
  </div>

  <div class="panel panel--navy">
    <div class="boats-title">Boote</div>
    <p class="small">Unsere Boote Safiran und Lumara 1, ganz auf die Bedürfnisse von Tauchern und Schnorchler abgestimmt.</p>
    <div class="boat-pair">
      <div class="photo" role="img" aria-label="Foto: weisse Tauchyacht auf dem Meer" style="background:linear-gradient(180deg,#9cc6e6,#2e6fa8)"></div>
      <div class="photo" role="img" aria-label="Foto: Sonnendeck der Yacht" style="background:linear-gradient(180deg,#b9c9d6,#7a5a3e)"></div>
    </div>
    <div class="boat-name">▸ MY Lumara 1, Baujahr 2021.</div>
    <p class="small">Mit einer Länge von 32 Meter und 8 Meter Breite bietet das aus Stahl konstruierte Boot bequem Platz für 24 Gäste. 8 Kabinen mit zwei Einzelbetten befinden sich im Unterdeck und 4 Kabinen auf dem Oberdeck.</p>
    <div class="boat-pair">
      <div class="photo" role="img" aria-label="Foto: Yacht in Fahrt auf blauem Wasser" style="background:linear-gradient(180deg,#6fa0cf,#1e3f70)"></div>
      <div class="photo" role="img" aria-label="Foto: Salon im Innenraum der Yacht" style="background:linear-gradient(135deg,#3a2e22,#b08a52)"></div>
    </div>
    <div class="boat-name">▸ MY Safiran, Baujahr 2019.</div>
    <p class="small">Mit einer Länge von 30 Metern und einer Breite von 8 Metern bietet das aus Stahl konstruierte Boot bequem Platz für 22 Gäste. 5 Kabinen mit zwei Einzelbetten und 2 Doppelbettkabinen befinden sich im Unterdeck und 4 Einzelbettkabinen auf dem Oberdeck.</p>
    <div class="note">
      <p><span class="warn">(Das folgende trifft für beide Boote zu)</span><br>Im Restaurant auf dem Hauptdeck werden 3 Buffets pro Tag serviert und auf dem grosszügigen Tauchdeck macht man sich für die Abenteuer bereit. Auf dem Oberdeck gibt es viele schattige Sitzmöglichkeiten und eine Bar für ein gemütliches Zusammensein und zum Entspannen.</p>
      <p>Auf dem Topdeck warten gemütliche Liegen, ideal, um die Sonne zu geniessen oder die Sterne zu beobachten.</p>
    </div>
  </div>

  <div class="panel panel--blue stack" style="background:linear-gradient(180deg,var(--blue),#1a4f95)">
    <div class="card"><div class="card-title">Merohan, Fury Shoals</div><p>Zwei Stunden mit dem Boot vom Hafen Hamata entfernt liegt das Riff von Merohan, Heimat einer grossen Schule von Spinnerdelfinen. Mit uns hast du die Möglichkeit, mit den Delfinen in ihrer natürlichen Umgebung zu schwimmen und zu schnorcheln.</p></div>
    <div class="card"><div class="card-title">Vollcharter</div><p>Verbringe eine Woche als Vollcharter in Merohan und/oder Fury Shoals. Schnorcheln, Tauchen, die Zeit geniessen. Unsere Boote bieten viel Platz für Ruhe, Meditation oder Yoga. Die Region eignet sich hervorragend für die ganze Familie.</p></div>
    <div class="card"><div class="card-title">Mini-Safari</div><p>Zwei Nächte auf dem Meer, perfekt zum Schnorcheln und Tauchen an verschiedenen Orten in Fury Shoals.</p></div>
    <div class="card"><div class="card-title">Overnight</div><p>Mach eine kurze Pause. Geniesse die Sonne, die Sterne und das Meer. Erlebe die Schönheit von Merohan und verbringe eine Nacht auf dem Boot. Erforsche die farbenfrohen Riffe während deiner Tauchgänge oder schwimme und schnorchle mit den Delfinen und lass sie deine Seele berühren.</p></div>
    <div class="photo" role="img" aria-label="Foto: Taucher zwischen orangen Fischschwärmen und Korallen" style="left:0;right:0;bottom:0;height:185px;background:linear-gradient(180deg,#1a4f95 0%,#1f6fb6 40%,#0f3a70 100%)"></div>
  </div>
</section>

</body>
</html>
```